Sports & fitness accessories website needs web design

We have a prestashop website that needs an appropriate skin that will work on the site and translate onto tarvik and qolm shops.
The site is currently live www.dolbrane.co.uk
Target Market(s)
Sports & fitness enthusiasts
Industry/Entity Type
Fitness
Number of Pages Required
5+ page
Font styles to use
Sans Serif

```html
<!DOCTYPE html>
<html lang="en">
<head>
<meta charset="utf-8">
<title>Dolbrane – Sports &amp; Fitness Accessories</title>
<link href="https://fonts.googleapis.com/css2?family=Open+Sans:wght@400;600;700&family=Oswald:wght@500;600&family=PT+Serif&display=swap" rel="stylesheet">
<style>
:root{
  --orange:#f07c1b;
  --ink:#333333;
  --muted:#9a9a9a;
  --line:#e6e6e6;
  --footer:#242424;
  --footer-base:#1a1a1a;
  --footer-text:#8a8a8a;
  --white:#ffffff;
}
*{margin:0;padding:0;box-sizing:border-box}
html,body{width:803px;height:1200px;overflow:hidden;background:var(--white)}
body{position:relative;font-family:"Open Sans",Arial,sans-serif;color:var(--ink)}
.abs{position:absolute}
.header{left:0;top:0;width:803px;height:66px;background:linear-gradient(#fafafa,#f2f2f2)}
.logo{left:74px;top:10px;width:92px;height:44px;background:var(--white);display:flex;align-items:center;justify-content:center;gap:5px;font-weight:700;font-size:13px;color:#555}
.logo i{width:9px;height:9px;background:#555;display:block}
.toplinks{left:348px;top:12px;display:flex;gap:15px;font-size:8px;color:var(--muted);align-items:center}
.toplinks b{color:#555;font-weight:700}
.toplinks .bag{display:flex;align-items:center;gap:5px}
.toplinks .bag span.dot{width:13px;height:13px;border-radius:50%;background:#999}
.search{left:522px;top:34px;width:201px;height:20px;border-radius:10px;background:var(--white);border:1px solid #ececec;font-size:8px;font-style:italic;color:#aaa;padding:4px 9px}
.search svg{position:absolute;right:7px;top:4px}
.nav{left:74px;top:66px;width:656px;height:47px;display:flex;justify-content:space-between;align-items:center;padding:0 16px;font-size:9px;text-transform:uppercase}
.nav .on{color:var(--orange)}
.rule{left:0;width:803px;height:1px;background:var(--line)}
.hero{left:74px;top:110px;width:656px;height:261px;background:linear-gradient(100deg,#e69a4a 0%,#d88a3c 30%,#8a4a22 60%,#3b2418 100%)}
.promo{left:89px;top:159px;width:320px;height:151px;background:linear-gradient(90deg,rgba(0,0,0,.85) 60%,rgba(0,0,0,0));padding:12px 12px}
.promo h1{font-family:"Oswald",sans-serif;font-weight:600;color:var(--white);font-size:29px;line-height:36px;letter-spacing:.5px}
.promo p{font-family:"Oswald",sans-serif;font-weight:500;color:var(--orange);font-size:17px;margin-top:2px}
.promo a{display:inline-block;margin-top:10px;border:1px solid var(--white);color:var(--white);font-size:8px;font-weight:700;padding:6px 8px}
.cats{left:74px;top:372px;width:656px;height:121px;display:flex}
.cat{position:relative;height:100%;display:flex;flex-direction:column;align-items:center;justify-content:center;color:var(--white);font-size:11px;font-weight:600;text-transform:uppercase;gap:5px}
.cat span.img{position:absolute;inset:0;z-index:0}
.cat svg,.cat em{position:relative;z-index:1;font-style:normal}
.arrow{top:421px;width:25px;height:25px}
.sec-title{left:0;top:517px;width:803px;text-align:center;font-size:14px;font-weight:400;color:#444;letter-spacing:.3px}
.sec-title::before,.sec-title::after{content:"·";color:#ccc;margin:0 10px}
.shade{left:80px;top:550px;width:643px;height:12px;background:radial-gradient(ellipse at top,rgba(0,0,0,.05),transparent 70%)}
.product{width:140px;text-align:center}
.product .pic{width:90px;height:80px;margin:0 auto;border-radius:8px}
.product h3{font-weight:400;font-size:9px;margin-top:21px}
.product .price{color:var(--orange);font-size:13px;margin-top:2px}
.product .cart{font-size:7px;font-weight:600;margin-top:4px}
.footer{left:0;top:1008px;width:803px;height:161px;background:var(--footer)}
.fcol{color:var(--footer-text);font-size:8px;line-height:16px}
.fcol h4{font-family:"PT Serif",serif;font-weight:400;color:var(--white);font-size:12px;margin-bottom:4px}
.email{width:152px;height:23px;background:var(--white);font-size:7px;font-style:italic;color:#888;padding:6px 8px;margin-top:14px}
.btn{display:inline-block;margin-top:8px;background:#6a6a6a;color:var(--white);font-family:"PT Serif",serif;font-size:12px;padding:2px 9px}
.social{display:grid;grid-template-columns:repeat(5,20px);gap:9px 9px}
.social i{width:20px;height:20px;border:1px solid #3c3c3c;display:block}
.social i.on{background:#3b5ba5;border-color:#3b5ba5}
.base{left:0;top:1169px;width:803px;height:31px;background:var(--footer-base);color:var(--footer-text);font-size:8px;padding:10px 76px}
.cards{right:74px;top:1177px;display:flex;gap:3px}
.cards span{width:25px;height:16px;background:var(--white);font-size:5px;font-weight:700;color:#333;display:flex;align-items:center;justify-content:center}
</style>
</head>
<body>
<header class="abs header"></header>
<div class="abs logo"><i></i>Dolbrane</div>
<div class="abs toplinks"><span>LOGIN</span><span>MY ACCOUNT</span><span>VIEW CART</span><span>CHECKOUT</span><span class="bag"><span class="dot"></span><b>SHOPPING BAG</b> (9 ITEMS) - <b>$10.00</b></span></div>
<div class="abs search">Search entire store...<svg width="10" height="10" viewBox="0 0 10 10"><circle cx="4" cy="4" r="3" fill="none" stroke="#bbb" stroke-width="1.2"/><path d="M6.3 6.3L9 9" stroke="#bbb" stroke-width="1.2"/></svg></div>
<div class="abs rule" style="top:66px"></div>
<nav class="abs nav"><span class="on">Home</span><span>Gym Acc</span><span>Fitness Acc</span><span>Weights</span><span>Yoga</span><span>Swimming</span><span>Training</span><span>Footwear</span><span>Sale</span></nav>
<div class="abs rule" style="top:113px"></div>

<div class="abs hero" role="img" aria-label="Runner's shoes on a sunlit road at sunset"></div>
<div class="abs promo">
  <h1>START YOUR JOURNEY<br>WITH DOLBRANE</h1>
  <p>A FURTHER 20% OFF SLECTED ITEMS</p>
  <a>SHOP NOW</a>
</div>

<div class="abs rule" style="top:472px"></div>
<div class="abs cats">
  <div class="cat" style="width:157px"><span class="img" role="img" aria-label="Fitness class photo" style="background:#5e6577"></span>
    <svg width="18" height="28" viewBox="0 0 18 28"><rect x="2" y="6" width="14" height="16" rx="3" fill="none" stroke="#fff" stroke-width="2"/><rect x="5" y="1" width="8" height="5" fill="#fff"/><rect x="5" y="22" width="8" height="5" fill="#fff"/></svg><em>Fitness</em></div>
  <div class="cat" style="width:160px"><span class="img" role="img" aria-label="Weights gym photo" style="background:#3a3e44"></span>
    <svg width="26" height="26" viewBox="0 0 26 26"><path d="M6 20L20 6" stroke="#fff" stroke-width="4"/><path d="M2 18l6 6M18 2l6 6" stroke="#fff" stroke-width="4"/></svg><em>Wieghts</em></div>
  <div class="cat" style="width:167px"><span class="img" role="img" aria-label="Yoga meditation photo" style="background:#4a4e5e"></span>
    <svg width="26" height="26" viewBox="0 0 26 26"><circle cx="13" cy="5" r="4" fill="#fff"/><path d="M5 18q8-14 16 0zM2 22h22v3H2z" fill="#fff"/></svg><em>Yoga</em></div>
  <div class="cat" style="width:172px"><span class="img" role="img" aria-label="Swimmer in pool photo" style="background:#4f6f86"></span>
    <svg width="34" height="22" viewBox="0 0 34 22"><circle cx="26" cy="5" r="4" fill="#fff"/><path d="M6 12l10-8 6 6" fill="none" stroke="#fff" stroke-width="3"/><path d="M1 15q4-3 8 0t8 0 8 0 8 0M1 20q4-3 8 0t8 0 8 0 8 0" fill="none" stroke="#fff" stroke-width="2"/></svg><em>Swimming</em></div>
</div>
<svg class="abs arrow" style="left:29px" viewBox="0 0 25 25"><circle cx="12.5" cy="12.5" r="12.5" fill="#444"/><path d="M18 12.5H8M12 7.5l-5 5 5 5" fill="none" stroke="#fff" stroke-width="2.6"/></svg>
<svg class="abs arrow" style="left:751px" viewBox="0 0 25 25"><circle cx="12.5" cy="12.5" r="12.5" fill="#444"/><path d="M7 12.5h10M13 7.5l5 5-5 5" fill="none" stroke="#fff" stroke-width="2.6"/></svg>

<h2 class="abs sec-title">FEATURED PRODUCTS</h2>
<div class="abs shade"></div>

<div class="abs product" style="left:91px;top:612px"><div class="pic" role="img" aria-label="Wrist and ankle weights" style="background:linear-gradient(#c9ccd4,#7d8cc0)"></div><h3>Yarrow Wrist &amp; Ankle</h3><div class="price">$ 1234</div><div class="cart">ADD TO CART</div></div>
<div class="abs product" style="left:252px;top:612px"><div class="pic" role="img" aria-label="Swimming kickboard" style="background:linear-gradient(90deg,#3d62b0,#e88a2a,#3d62b0);width:60px"></div><h3 style="margin-top:19px">Kickboard</h3><div class="price">$ 1234</div><div class="cart">ADD TO CART</div></div>
<div class="abs product" style="left:412px;top:612px"><div class="pic" role="img" aria-label="Arch support on a foot" style="background:linear-gradient(#e0b6a2,#2a2a2a)"></div><h3 style="margin-top:19px">Arch Supports</h3><div class="price">$ 1234</div><div class="cart">ADD TO CART</div></div>
<div class="abs product" style="left:573px;top:612px"><div class="pic" role="img" aria-label="Sit up bar" style="background:linear-gradient(#3a3a3a,#777)"></div><h3>Sit Up Bar</h3><div class="price">$ 1234</div><div class="cart">ADD TO CART</div></div>

<div class="abs product" style="left:91px;top:821px"><div class="pic" role="img" aria-label="Wrist and ankle weights" style="background:linear-gradient(#c9ccd4,#7d8cc0)"></div><h3>Yarrow Wrist &amp; Ankle</h3><div class="price">$ 1234</div><div class="cart">ADD TO CART</div></div>
<div class="abs product" style="left:252px;top:821px"><div class="pic" role="img" aria-label="Swimming kickboard" style="background:linear-gradient(90deg,#3d62b0,#e88a2a,#3d62b0);width:60px"></div><h3 style="margin-top:19px">Kickboard</h3><div class="price">$ 1234</div><div class="cart">ADD TO CART</div></div>
<div class="abs product" style="left:412px;top:821px"><div class="pic" role="img" aria-label="Arch support on a foot" style="background:linear-gradient(#e0b6a2,#2a2a2a)"></div><h3 style="margin-top:19px">Arch Supports</h3><div class="price">$ 1234</div><div class="cart">ADD TO CART</div></div>
<div class="abs product" style="left:573px;top:821px"><div class="pic" role="img" aria-label="Sit up bar" style="background:linear-gradient(#3a3a3a,#777)"></div><h3>Sit Up Bar</h3><div class="price">$ 1234</div><div class="cart">ADD TO CART</div></div>

<footer class="abs footer"></footer>
<div class="abs fcol" style="left:76px;top:1030px;width:220px"><h4>Keep Me Posted</h4><p style="line-height:13px">Subscribe to our newsletter and always be the first to hear about what is happening at Iron Vale.</p><div class="email">Enter your email address..</div><span class="btn">Subscribe</span></div>
<div class="abs fcol" style="left:331px;top:1030px"><h4>Site Links</h4>Home<br>About Us<br>Featured Products<br>Contact Us</div>
<div class="abs fcol" style="left:472px;top:1030px"><h4>Help</h4>Lorem Ipsum Dolor<br>Sit Amet Consectetur<br>Adipsicing Elit<h4 style="margin-top:9px">Region</h4><span style="display:inline-block;width:9px;height:9px;border-radius:50%;background:#5a9bd0;vertical-align:middle"></span> Global ▾</div>
<div class="abs fcol" style="left:596px;top:1030px"><h4>Follow Us</h4><div class="social"><i class="on"></i><i></i><i></i><i></i><i></i><i></i><i></i><i></i></div></div>

<div class="abs base">Copyrights ©2014 dolbrane.co.uk - All Rights reserved</div>
<div class="abs cards"><span>Merix</span><span>Amvia</span><span>Paloo</span><span>Vesk</span></div>
</body>
</html>
```